Resort Room Letter to go in Welcome Basket

It needs the Resort Logo and a snazzier font. Probably some kind of background. It will be in full color. Dimensions 5.5in x 8in. This is the in room letter that goes with the welcome basket.

Text:

Welcome to The Resort! We have prepared this convenient Starter Pack to enhance your stay in our Luxury Condominiums. To further enhance your stay housekeeping will provide daily limited service which includes fresh towels and trash removal. Additional housekeeping services can be scheduled with the front desk for a nominal fee. Please leave the basket so that we can prepare a Starter Pack for the next guest. When you are ready to checkout simply dial **47.

Helpful Hints:

Turn the lever in the freezer to start making ice
The Waterpark can be accessed from the 1st Floor
The Indoor Waterpark is open from 9AM to 11PM
Vending with Snacks & Drinks are available on Floors 1, 2, 4, & 5
The closest grocery store is Brindlemart
You can also conveniently order groceries via Pantrygo from Halvey, Grain Town, & Tamrel
Additional convenience items are available for purchase at the Front Desk
Use our Express Checkout by Dialing **47

Thank you so much for choosing the Resort for your Smoky Mountain Vacation!

The Resort Management Team

```html
<!DOCTYPE html>
<html lang="en">
<head>
<meta charset="utf-8">
<title>Welcome Letter – Three Versions</title>
<link href="https://fonts.googleapis.com/css2?family=Libre+Baskerville:wght@700&family=Mulish:wght@400;700&family=Archivo:wght@700&display=swap" rel="stylesheet">
<style>
  :root{
    --board:#bdbdbd;
    --label:#111111;
    --teal:#3f6b79;
    --ink:#4e4e4e;
    --brown:#4b3a2f;
    --wood-dark:#5e4a3b;
    --bamboo:#d8a45c;
    --cream:#fbe7c9;
    --white:#ffffff;
  }
  *{box-sizing:border-box;margin:0;padding:0}
  html,body{width:1200px;height:684px;overflow:hidden;background:var(--board)}
  .board{position:relative;width:1200px;height:684px}

  .letter{position:absolute;top:25px;width:372px;height:540px;background:var(--white);overflow:hidden}
  .letter--plain{left:25px}
  .letter--framed{left:414px}
  .letter--bamboo{left:803px;background:var(--wood-dark)}

  .content{position:absolute;left:0;right:0;top:0;bottom:0;text-align:center;font-family:"Mulish",sans-serif;color:var(--ink)}
  .brand{height:88px;padding-top:40px;font-family:"Mulish",sans-serif;font-weight:700;font-size:14px;letter-spacing:1px;text-transform:uppercase}
  .welcome{font-family:"Libre Baskerville",serif;font-weight:700;font-size:24px;letter-spacing:5px;margin-top:22px;line-height:1}
  .welcome-sub{font-family:"Libre Baskerville",serif;font-size:11px;letter-spacing:1px;margin-top:6px}
  .intro{font-size:9.2px;line-height:11.6px;margin:12px auto 0;width:262px}
  .hints-title{font-family:"Libre Baskerville",serif;font-weight:700;font-size:11px;letter-spacing:2px;margin-top:18px}
  .hints{list-style:none;text-align:left;margin:12px auto 0;width:258px;font-size:8.6px;line-height:10.4px}
  .hints li{position:relative;padding-left:14px;margin-bottom:1.6px}
  .hints li::before{content:"";position:absolute;left:0;top:1px;width:8px;height:8px;border-radius:50%;background:var(--check)}
  .hints li::after{content:"";position:absolute;left:2.6px;top:2.6px;width:2px;height:3.5px;border:solid var(--white);border-width:0 1.2px 1.2px 0;transform:rotate(45deg)}
  .thanks{font-family:"Libre Baskerville",serif;font-weight:700;font-size:10.5px;letter-spacing:2px;line-height:13.5px;margin:20px auto 0;width:230px;text-transform:uppercase}
  .signature{font-size:7.5px;letter-spacing:.5px;margin-top:24px;text-transform:uppercase}

  /* Version 01 */
  .letter--plain .content{--check:var(--teal)}
  .letter--plain .brand,.letter--plain .welcome,.letter--plain .welcome-sub,
  .letter--plain .hints-title,.letter--plain .thanks{color:var(--teal)}

  /* Version 02 */
  .letter--framed .content{--check:var(--brown)}
  .letter--framed .brand,.letter--framed .welcome,.letter--framed .welcome-sub,
  .letter--framed .hints-title,.letter--framed .thanks{color:var(--brown)}
  .frame-outer{position:absolute;inset:9px;border:3px solid var(--brown);border-radius:4px}
  .frame-inner{position:absolute;inset:15px;border:1px solid var(--brown)}
  .corner-star{position:absolute;width:14px;height:14px;fill:var(--brown)}
  .corner-star--tl{left:3px;top:3px}.corner-star--tr{right:3px;top:3px}
  .corner-star--bl{left:3px;bottom:3px}.corner-star--br{right:3px;bottom:3px}

  /* Version 03 */
  .bamboo-frame{position:absolute;left:10px;top:10px;width:352px;height:498px;background:var(--bamboo);border-radius:6px}
  .panel{position:absolute;left:24px;top:22px;width:324px;height:474px;background:var(--cream)}
  .letter--bamboo .content{--check:var(--brown);color:var(--ink)}
  .letter--bamboo .brand,.letter--bamboo .welcome,.letter--bamboo .welcome-sub,
  .letter--bamboo .hints-title,.letter--bamboo .thanks{color:var(--brown)}
  .letter--bamboo .intro{width:236px}
  .letter--bamboo .hints{width:236px}
  .letter--bamboo .thanks{margin-top:14px}
  .letter--bamboo .signature{color:var(--white);font-weight:700;margin-top:34px}

  .version-label{position:absolute;top:600px;width:372px;text-align:center;font-family:"Archivo",sans-serif;font-weight:700;font-size:42px;letter-spacing:1px;color:var(--label)}
  .version-label--one{left:25px}.version-label--two{left:414px}.version-label--three{left:803px}
</style>
</head>
<body>
<main class="board">

  <!-- Version 01 -->
  <article class="letter letter--plain">
    <div class="content">
      <div class="brand">The Resort at Ashford Ridge</div>
      <h1 class="welcome">WELCOME</h1>
      <p class="welcome-sub">TO THE RESORT!</p>
      <p class="intro">We have prepared this convenient Starter Pack to enhance your stay in our Luxury Condominiums. To further enhance your stay housekeeping will provide daily limited service which includes fresh towels and trash removal. Additional housekeeping services can be scheduled with the front desk for a nominal fee. Please leave the basket so that we can prepare a Starter Pack for the next guest.</p>
      <h2 class="hints-title">HELPFUL HINTS:</h2>
      <ul class="hints">
        <li>Turn the lever in the freezer to start making ice</li>
        <li>The Waterpark can be accessed from the 1st Floor</li>
        <li>The Indoor Waterpark is open from 9AM to 11PM</li>
        <li>Vending with Snacks &amp; Drinks are available on Floors 1, 2, 4, &amp; 5</li>
        <li>The closest grocery store is Brindlemart</li>
        <li>You can also conveniently order groceries via Pantrygo from Halvey, Grain Town, &amp; Tamrel</li>
        <li>Additional convenience items are available for purchase at the Front Desk</li>
        <li>Use our Express Checkout by Dialing **47</li>
      </ul>
      <p class="thanks">Thank you so much for choosing the Resort for your Smoky Mountain Vacation!</p>
      <p class="signature">- The Resort Management Team</p>
    </div>
  </article>

  <!-- Version 02 -->
  <article class="letter letter--framed">
    <div class="frame-outer"></div>
    <div class="frame-inner"></div>
    <svg class="corner-star corner-star--tl" viewBox="0 0 20 20"><polygon points="10,1 12.6,7.3 19.5,7.6 14.1,11.9 16,18.6 10,14.8 4,18.6 5.9,11.9 0.5,7.6 7.4,7.3"/></svg>
    <svg class="corner-star corner-star--tr" viewBox="0 0 20 20"><polygon points="10,1 12.6,7.3 19.5,7.6 14.1,11.9 16,18.6 10,14.8 4,18.6 5.9,11.9 0.5,7.6 7.4,7.3"/></svg>
    <svg class="corner-star corner-star--bl" viewBox="0 0 20 20"><polygon points="10,1 12.6,7.3 19.5,7.6 14.1,11.9 16,18.6 10,14.8 4,18.6 5.9,11.9 0.5,7.6 7.4,7.3"/></svg>
    <svg class="corner-star corner-star--br" viewBox="0 0 20 20"><polygon points="10,1 12.6,7.3 19.5,7.6 14.1,11.9 16,18.6 10,14.8 4,18.6 5.9,11.9 0.5,7.6 7.4,7.3"/></svg>
    <div class="content">
      <div class="brand">The Resort at Ashford Ridge</div>
      <h1 class="welcome">WELCOME</h1>
      <p class="welcome-sub">TO THE RESORT!</p>
      <p class="intro">We have prepared this convenient Starter Pack to enhance your stay in our Luxury Condominiums. To further enhance your stay housekeeping will provide daily limited service which includes fresh towels and trash removal. Additional housekeeping services can be scheduled with the front desk for a nominal fee. Please leave the basket so that we can prepare a Starter Pack for the next guest.</p>
      <h2 class="hints-title">HELPFUL HINTS:</h2>
      <ul class="hints">
        <li>Turn the lever in the freezer to start making ice</li>
        <li>The Waterpark can be accessed from the 1st Floor</li>
        <li>The Indoor Waterpark is open from 9AM to 11PM</li>
        <li>Vending with Snacks &amp; Drinks are available on Floors 1, 2, 4, &amp; 5</li>
        <li>The closest grocery store is Brindlemart</li>
        <li>You can also conveniently order groceries via Pantrygo from Halvey, Grain Town, &amp; Tamrel</li>
        <li>Additional convenience items are available for purchase at the Front Desk</li>
        <li>Use our Express Checkout by Dialing **47</li>
      </ul>
      <p class="thanks">Thank you so much for choosing the Resort for your Smoky Mountain Vacation!</p>
      <p class="signature">- The Resort Management Team</p>
    </div>
  </article>

  <!-- Version 03 -->
  <article class="letter letter--bamboo">
    <div class="bamboo-frame" role="img" aria-label="Illustrated bamboo pole frame lashed at the corners"></div>
    <div class="panel"></div>
    <div class="content">
      <div class="brand">The Resort at Ashford Ridge</div>
      <h1 class="welcome">WELCOME</h1>
      <p class="welcome-sub">TO THE RESORT!</p>
      <p class="intro">We have prepared this convenient Starter Pack to enhance your stay in our Luxury Condominiums. To further enhance your stay housekeeping will provide daily limited service which includes fresh towels and trash removal. Additional housekeeping services can be scheduled with the front desk for a nominal fee. Please leave the basket so that we can prepare a Starter Pack for the next guest.</p>
      <h2 class="hints-title">HELPFUL HINTS:</h2>
      <ul class="hints">
        <li>Turn the lever in the freezer to start making ice</li>
        <li>The Waterpark can be accessed from the 1st Floor</li>
        <li>The Indoor Waterpark is open from 9AM to 11PM</li>
        <li>Vending with Snacks &amp; Drinks are available on Floors 1, 2, 4, &amp; 5</li>
        <li>The closest grocery store is Brindlemart</li>
        <li>You can also conveniently order groceries via Pantrygo from Halvey, Grain Town, &amp; Tamrel</li>
        <li>Additional convenience items are available for purchase at the Front Desk</li>
        <li>Use our Express Checkout by Dialing **47</li>
      </ul>
      <p class="thanks">Thank you so much for choosing the Resort for your Smoky Mountain Vacation!</p>
      <p class="signature">- The Resort Management Team</p>
    </div>
  </article>

  <p class="version-label version-label--one">VERSION 01</p>
  <p class="version-label version-label--two">VERSION 02</p>
  <p class="version-label version-label--three">VERSION 03</p>
</main>
</body>
</html>
```